A website design for a consultation firm

We are located in Istanbul, Turkey and offers our consultation services to customers interested in investing in Realestate, Education and Investment particularly this coming from Arab world and English speaking countries.

The site should carry our message of deep knowledge about the Turkish markets in the mentioned sectors of interest, sincerity and keenness.

The final deliverable of the winning design should include:
- The source files of the final designs. e.g. AI, PSD ..etc
- The redline markup for the design using a Specctr or any other similar tool.

Target Market(s)

English and Arabic speaking countries with a Turkish theme since we are a Turkish company

Industry/Entity Type

Consulting

Number of Pages Required

2 page

Font styles to use
Sans Serif

Requirements
Must have
• The site should serve the following main sections:
• - Why QVE?
• - Reports & studies
• - Sectors
• - Our team
• - Contact
• We need a design that could be converted into a WordPress theme.
• The design should be in English but should accommodate other languages including RTL.
• You can use the color theme you like as long as it does't dissolve the logo.
• The site should link into our accounts on the following networks:
• - Chirpline
• - Friendspace
• - LinkedIn
• The design should be responsive and nicely rendered on Desktop, Tablets and Smart phones.
Nice to have
• The site would be nice to balance between being informative and

```html
<!DOCTYPE html>
<html lang="en">
<head>
<meta charset="utf-8">
<title>QVE Consulting</title>
<link href="https://fonts.googleapis.com/css2?family=Raleway:wght@400;500;600;700&family=Open+Sans:wght@400;600&display=swap" rel="stylesheet">
<style>
:root{
  --red:#c8001e;
  --red-dark:#a80019;
  --navy:#14306e;
  --navy-btn:#0d2a6b;
  --footer:#0f3a8c;
  --footer-bar:#1a4ba0;
  --grey:#e0e0e0;
  --text:#555;
  --white:#fff;
}
*{box-sizing:border-box;margin:0;padding:0}
html,body{width:707px;height:1200px;overflow:hidden}
body{position:relative;background:var(--white);font-family:"Open Sans",Arial,sans-serif;color:var(--text)}
.abs{position:absolute}

.site-header{left:0;top:0;width:707px;height:64px;background:var(--white);z-index:3}
.brand{left:78px;top:18px;display:flex;align-items:center;gap:8px;z-index:4}
.brand-dot{width:16px;height:16px;border-radius:50%;background:var(--red)}
.brand-name{font-family:"Raleway",sans-serif;font-weight:700;font-size:26px;color:var(--red);letter-spacing:1px}
.lang{left:591px;top:7px;font-family:"Raleway",sans-serif;font-size:8.5px;font-weight:600;color:#222}
.main-nav{top:32px;left:0;width:707px;font-family:"Raleway",sans-serif;font-size:9.6px;font-weight:500;color:#666}
.main-nav a{position:absolute;color:inherit;text-decoration:none;white-space:nowrap}
.main-nav a.active{color:var(--navy);font-weight:600}
.nav-underline{left:242px;top:61px;width:38px;height:3px;background:var(--navy)}

.hero{left:0;top:64px;width:707px;height:276px;background:linear-gradient(180deg,#e08a14 0%,#9a4a1a 22%,#3a1e22 45%,#1a1420 70%,#2b1d1c 100%)}
.hero-title{left:184px;top:177px;width:338px;height:43px;background:rgba(20,48,110,.82);color:var(--white);font-family:"Raleway",sans-serif;font-weight:700;font-size:24px;display:flex;align-items:center;justify-content:center;letter-spacing:.5px}
.hero-arrow{top:186px}

.service-band{left:0;top:340px;z-index:1}
.service-pins{left:0;top:300px;z-index:2}
.services{left:0;top:340px;width:707px;height:164px;z-index:2}
.service{position:absolute;top:0;width:180px;text-align:center;color:var(--white)}
.service-title{position:absolute;top:67px;left:0;width:180px;font-family:"Raleway",sans-serif;font-weight:600;font-size:10.5px;line-height:14px}
.service-text{position:absolute;top:100px;left:20px;width:140px;font-size:8.4px;line-height:12px;color:#fbe2e5}

.why{left:0;top:504px;width:353px;height:242px;background:var(--grey)}
.why-photo{left:353px;top:504px;width:354px;height:242px;background:linear-gradient(135deg,#e9eef3 0%,#c9d2da 45%,#8f9aa6 100%)}
.why h2{position:absolute;left:74px;top:42px;font-family:"Raleway",sans-serif;font-weight:400;font-size:17.6px;color:#222}
.why p{position:absolute;left:74px;width:270px;font-size:8.6px;line-height:14.4px;color:#555}
.btn{position:absolute;left:74px;top:174px;width:82px;height:25px;background:var(--navy-btn);color:var(--white);font-family:"Raleway",sans-serif;font-weight:600;font-size:8.8px;display:flex;align-items:center;justify-content:center}

.reports-title{left:75px;top:762px;font-family:"Raleway",sans-serif;font-size:17px;font-weight:500;color:var(--navy)}
.card{position:absolute;top:794px;width:174px;height:181px;border:1px solid #d0d0d0;background:var(--white)}
.card-img{height:88px;background:linear-gradient(135deg,#dfe4ea,#9aa6b3)}
.card h3{position:absolute;left:13px;top:100px;font-weight:400;font-size:10.3px;color:var(--navy)}
.card p{position:absolute;left:13px;top:116px;width:152px;font-size:7.4px;line-height:12px;color:#888}
.card .more{position:absolute;left:13px;top:154px;font-size:7.6px;font-weight:600;color:var(--red)}

.site-footer{left:0;top:1005px;width:707px;height:161px;background:var(--footer);color:var(--white)}
.site-footer h4{position:absolute;top:30px;font-family:"Raleway",sans-serif;font-weight:600;font-size:10px}
.f-links{position:absolute;left:82px;top:55px;list-style:none;font-size:8.3px;line-height:16px}
.f-contact{position:absolute;left:225px;top:55px;font-size:7.3px;line-height:11px}
.f-row{display:flex;gap:8px;margin-bottom:8px;align-items:flex-start}
.f-posts{position:absolute;left:411px;top:54px;width:150px}
.post{margin-bottom:10px}
.post-title{font-size:8.2px}
.post-text{font-size:6.4px;line-height:9px;color:#dbe4f5}
.post-date{font-size:6.2px;color:#a9bde4;margin-top:3px}
.f-social{position:absolute;left:579px;top:54px;font-size:7.8px}
.soc{display:flex;align-items:center;gap:7px;margin-bottom:6px}
.soc i{display:block;width:14px;height:14px;border:1px solid var(--white);border-radius:50%}
.footer-bar{left:0;top:1166px;width:707px;height:34px;background:var(--footer-bar);color:#b7c8ea;font-size:6.6px;text-align:center;padding-top:12px}
</style>
</head>
<body>

<header class="abs site-header">
  <div class="abs lang">EN &nbsp;| &nbsp;AR</div>
  <nav class="abs main-nav">
    <a class="active" style="left:248px">HOME</a>
    <a style="left:293px">WHY QVE?</a>
    <a style="left:354px">REPORTS &amp; STUDIES</a>
    <a style="left:462px">SECTORS</a>
    <a style="left:521px">OUR TEAM</a>
    <a style="left:586px">CONTACT</a>
  </nav>
  <div class="abs nav-underline"></div>
</header>
<div class="abs brand"><span class="brand-dot"></span><span class="brand-name">QVE</span></div>

<section class="abs hero" role="img" aria-label="Night view of a lit suspension bridge over the Bosphorus at sunset"></section>
<div class="abs hero-title">PROPERTY CONSULTING</div>
<svg class="abs hero-arrow" style="left:78px" width="14" height="22" viewBox="0 0 14 22"><path d="M12 2 3 11l9 9" fill="none" stroke="#fff" stroke-width="2.5"/></svg>
<svg class="abs hero-arrow" style="left:622px" width="14" height="22" viewBox="0 0 14 22"><path d="M2 2l9 9-9 9" fill="none" stroke="#fff" stroke-width="2.5"/></svg>

<svg class="abs service-band" width="707" height="190" viewBox="0 0 707 190">
  <path d="M0 0H707V164L353 186L220 164H0Z" fill="var(--red)"/>
  <path d="M220 164L353 186L707 164" fill="none" stroke="#e03049" stroke-width="1"/>
</svg>

<svg class="abs service-pins" width="707" height="110" viewBox="0 0 707 110">
  <g fill="#fff" stroke="var(--red-dark)" stroke-width="1">
    <path d="M146 74A34 34 0 1 1 186 74L166 96Z"/>
    <path d="M333 74A34 34 0 1 1 373 74L353 96Z"/>
    <path d="M520 74A34 34 0 1 1 560 74L540 96Z"/>
  </g>
  <g fill="none" stroke="var(--red)" stroke-width="2">
    <rect x="145" y="30" width="20" height="13" rx="2"/><path d="M150 43l-2 5 6-5"/>
    <path d="M151 36.5h2M155 36.5h2M159 36.5h2"/>
    <rect x="158" y="50" width="20" height="13" rx="2"/>
    <rect x="344" y="28" width="18" height="36"/>
    <path d="M348 34h4M354 34h4M348 40h4M354 40h4M348 46h4M354 46h4M348 52h4M354 52h4M350 58h6v6"/>
  </g>
  <g fill="var(--red)">
    <rect x="539" y="36" width="2.5" height="20"/>
    <path d="M540 44c-4-10-14-10-16-8 2 6 8 10 16 8Z"/>
    <path d="M541 44c4-10 14-10 16-8-2 6-8 10-16 8Z"/>
    <path d="M529 56h22l-3 7h-16Z"/>
  </g>
</svg>

<section class="abs services">
  <div class="service" style="left:76px"><div class="service-title">EDUCATION<br>CONSULTATION</div><div class="service-text">Class aptent taciti sociosqu ad litora torquent per conubia</div></div>
  <div class="service" style="left:263px"><div class="service-title">REAL ESTATE<br>CONSULTATION</div><div class="service-text">Class aptent taciti sociosqu ad litora torquent per conubia</div></div>
  <div class="service" style="left:450px"><div class="service-title">INVESTMENT<br>CONSULTING</div><div class="service-text">Class aptent taciti sociosqu ad litora torquent per conubia nostr</div></div>
</section>

<section class="abs why">
  <h2>WHY QVE?</h2>
  <p style="top:72px">Maecenas aliquet velit vel turpis Mauris neque metus malesuada nec ultricies sit amet porttitor mattis enim In massa</p>
  <p style="top:108px">cursus neque mi consectetuer mi a ultricies massa est sed nisl Class aptent taciti soaciosqu ad litora torquent per conubia nostra per inceptos hymenaeos Proin nulla arcu nonummy luctus dictum eget fermentum et lorem Nunc porta convallis ped</p>
  <a class="btn">LEARN MORE</a>
</section>
<div class="abs why-photo" role="img" aria-label="Business team in a bright meeting room discussing a project"></div>
<svg class="abs" style="left:0;top:503px" width="707" height="24" viewBox="0 0 707 24"><path d="M0 0H220L353 22L707 0Z" fill="var(--red)"/></svg>

<h2 class="abs reports-title">Reports &amp; Studies</h2>
<article class="card" style="left:75px"><div class="card-img" role="img" aria-label="Family working together at a laptop"></div><h3>Aorquent per conubia</h3><p>per inceptos hymenaeos Proin nulla arcu nonummy luctus dictum eget fermentum et lorem Nunc porta convallis pede</p><span class="more">READ MORE</span></article>
<article class="card" style="left:267px"><div class="card-img" role="img" aria-label="Presenter at a whiteboard before a seated team"></div><h3>Suspendisse risus nibh</h3><p>per inceptos hymenaeos Proin nulla arcu nonummy luctus dictum eget fermentum et lorem Nunc porta convallis pede</p><span class="more">READ MORE</span></article>
<article class="card" style="left:459px"><div class="card-img" role="img" aria-label="Colleagues reviewing a tablet in an office"></div><h3>Etiam eleifend metus h</h3><p>per inceptos hymenaeos Proin nulla arcu nonummy luctus dictum eget fermentum et lorem Nunc porta convallis pede</p><span class="more">READ MORE</span></article>

<footer class="abs site-footer">
  <h4 style="left:82px">QUICK LINKS</h4>
  <ul class="f-links"><li>Why QVE?</li><li>Reports &amp; studies</li><li>Sectors</li><li>Our team</li><li>Contact</li></ul>
  <h4 style="left:225px">CONTACT US</h4>
  <div class="f-contact">
    <div class="f-row"><svg width="10" height="12" viewBox="0 0 10 12"><path d="M5 11S1 7 1 4.5a4 4 0 0 1 8 0C9 7 5 11 5 11Z" fill="none" stroke="#fff"/><circle cx="5" cy="4.5" r="1.3" fill="none" stroke="#fff"/></svg><span>18 Harbor Lane Suite 200 Kadikoy,<br>IST 34710 Voice 212.555.0142</span></div>
    <div class="f-row"><svg width="11" height="10" viewBox="0 0 11 10"><path d="M2 1l2 2-1 2c1 1.5 2 2.5 3 3l2-1 2 2-1 1C5 10 1 6 1 2Z" fill="none" stroke="#fff" stroke-width=".9"/></svg><span>Phone:+90 212-555-0187</span></div>
    <div class="f-row"><svg width="11" height="9" viewBox="0 0 11 9"><rect x=".5" y=".5" width="10" height="8" fill="none" stroke="#fff"/><path d="M.5 .5l5 4 5-4" fill="none" stroke="#fff"/></svg><span>info@qveconsult.example</span></div>
  </div>
  <h4 style="left:412px">LATEST POSTS</h4>
  <div class="f-posts">
    <div class="post"><div class="post-title">In iaculis facilisis massa Etiam</div><div class="post-text">Nam cursus Morbi ut mi Nullam enim</div><div class="post-date">25 May 2016</div></div>
    <div class="post"><div class="post-title">Fusce tellus Sed</div><div class="post-text">pulvinar eu ante Integer orci tellus tristique vitae consequat nec</div><div class="post-date">25 May 2016</div></div>
  </div>
  <h4 style="left:579px">SOCIAL</h4>
  <div class="f-social">
    <div class="soc"><i></i>Friendspace</div>
    <div class="soc"><i></i>Chirpline</div>
    <div class="soc"><i></i>ProNet</div>
  </div>
</footer>
<div class="abs footer-bar">© 2016 Company Name &nbsp;All right reserved &nbsp;Term of Use</div>

</body>
</html>
```